Korvo Suplies

Packaging design for Multitool Blades, something similar to the drawing on paper, diecut of the packaging attached

Logo Text

Korvo Supplies

```html
<!DOCTYPE html>
<html lang="en">
<head>
<meta charset="utf-8">
<title>Korvo Supplies – Multitool Blade Packaging</title>
<link href="https://fonts.googleapis.com/css2?family=Montserrat:wght@700&display=swap" rel="stylesheet">
<style>
  :root {
    --pack-black: #000000;
    --pack-green: #7ac943;
    --ink: #000000;
  }
  html, body {
    margin: 0;
    padding: 0;
    width: 826px;
    height: 1200px;
    overflow: hidden;
    background: var(--pack-black);
  }
  .packaging {
    position: relative;
    width: 826px;
    height: 1200px;
    background: var(--pack-black);
    font-family: "Montserrat", sans-serif;
  }
  .hang-tab {
    position: absolute;
    left: 280px;
    top: 57px;
    width: 269px;
    height: 68px;
    border-radius: 34px;
    background: var(--pack-green);
  }
  .brand-panel {
    position: absolute;
    left: 131px;
    top: 214px;
    width: 567px;
    height: 188px;
    background: var(--pack-green);
    display: flex;
    align-items: center;
    justify-content: center;
  }
  .brand-name {
    margin: 0;
    color: var(--ink);
    font-weight: 700;
    font-size: 60px;
    letter-spacing: 0.5px;
    line-height: 1;
    white-space: nowrap;
  }
  .tool-window {
    position: absolute;
    left: 0;
    top: 0;
  }
  .tool-window .window-shape {
    fill: var(--pack-green);
  }
  .tool-window .window-label {
    fill: var(--ink);
    font-family: "Montserrat", sans-serif;
    font-weight: 700;
    font-size: 47px;
  }
  .blade-slots {
    position: absolute;
    left: 639px;
    top: 523px;
    display: flex;
    flex-direction: column;
    gap: 31px;
  }
  .blade-slot {
    width: 91px;
    height: 90px;
    background: var(--pack-green);
  }
</style>
</head>
<body>
  <main class="packaging">
    <div class="hang-tab"></div>

    <header class="brand-panel">
      <h1 class="brand-name">Korvo Supplies</h1>
    </header>

    <svg class="tool-window" width="826" height="1200" viewBox="0 0 826 1200" aria-label="Multitool cutout window">
      <path class="window-shape"
            d="M357,669 A110,110 0 1 1 471,669 Q478,900 556,1045 H272 Q350,900 357,669 Z"/>
      <text class="window-label" x="0" y="0" text-anchor="middle" dominant-baseline="central"
            transform="translate(414,763) rotate(-90)">Multitool Cutout</text>
    </svg>

    <div class="blade-slots">
      <div class="blade-slot"></div>
      <div class="blade-slot"></div>
      <div class="blade-slot"></div>
      <div class="blade-slot"></div>
    </div>
  </main>
</body>
</html>
```